Verpackungen für Temperatur-Kalibrierprodukte
Zielgruppe
Wir sind eine Firma, die Temperatur-Kalibrierprodukte vertreibt und suchen ein hochwertiges Design für die Verpackung unserer High-End Thermometer. Unsere Zielgruppe sind Firmen aus Industrie, Forschung und Entwicklung.
Aufgabenstellung
Wir suchen ein Design für eine Magnetbox, in der unsere hochwertigen Thermometer transportiert und aufbewahrt werden. Das Design soll sich an unsere Website-Gestaltung anlehnen, bzw. dazu passen.
Auf die Verpackung sollte das Logo, sowie das Wort 'Präzisionsthermometer'.
Innenmaße der Verpackung:
60 x 13 x 4,5 / 4,5 cm (Breite x Tiefe x Höhe/Klappenhöhe)
Material: 1,8 mm Graubpappe innen weiß
Bezugsmaterial: außen weißes Kraftpapier 157g
Bei Bedarf können wir weiteres Bildmaterial zur Verfügung stellen (siehe Website).

```html
<!DOCTYPE html>
<html lang="de">
<head>
<meta charset="utf-8">
<title>Termivo – Magnetbox Präzisionsthermometer</title>
<link rel="stylesheet" href="https://fonts.googleapis.com/css2?family=Montserrat:wght@400;500;700&display=swap">
<style>
  :root {
    --paper: #ffffff;
    --dieline: #4a4a4a;
    --ink: #1c1c1c;
    --mark: #3a3a3a;
    --silk-light: #f2f2f2;
    --silk-mid: #dcdcdc;
    --silk-dark: #b4b4b4;
    --red-deep: #7f1d22;
    --red-bright: #e07478;
    --band-text: #ffffff;
  }
  html, body {
    margin: 0;
    padding: 0;
    width: 1200px;
    height: 960px;
    overflow: hidden;
    background: var(--paper);
  }
  .dieline-sheet {
    display: block;
    width: 1200px;
    height: 960px;
  }
  .cut {
    fill: var(--paper);
    stroke: var(--dieline);
    stroke-width: 0.8;
  }
  .cut-open {
    fill: none;
    stroke: var(--dieline);
    stroke-width: 0.8;
  }
  .brand-name {
    font-family: "Montserrat", sans-serif;
    font-weight: 500;
    fill: var(--ink);
  }
  .brand-dot { fill: var(--mark); }
  .band-label {
    font-family: "Montserrat", sans-serif;
    font-size: 17px;
    fill: var(--band-text);
    letter-spacing: 0.4px;
  }
  .band-label .light { font-weight: 400; }
  .band-label .strong { font-weight: 700; }
</style>
</head>
<body>
<svg class="dieline-sheet" viewBox="0 0 1200 960" xmlns="http://www.w3.org/2000/svg">
  <defs>
    <linearGradient id="silkTone" x1="0" y1="0" x2="1" y2="1">
      <stop offset="0" stop-color="var(--silk-mid)"/>
      <stop offset="0.3" stop-color="var(--silk-light)"/>
      <stop offset="0.55" stop-color="var(--silk-dark)"/>
      <stop offset="0.8" stop-color="var(--silk-light)"/>
      <stop offset="1" stop-color="var(--silk-mid)"/>
    </linearGradient>
    <linearGradient id="ribbonTone" x1="0" y1="0" x2="1" y2="0.15">
      <stop offset="0" stop-color="var(--red-deep)"/>
      <stop offset="0.17" stop-color="var(--red-bright)"/>
      <stop offset="0.4" stop-color="var(--red-deep)"/>
      <stop offset="0.62" stop-color="var(--red-deep)"/>
      <stop offset="0.75" stop-color="var(--red-bright)"/>
      <stop offset="1" stop-color="var(--red-deep)"/>
    </linearGradient>
  </defs>

  <!-- side tuck flaps -->
  <g class="side-flap left">
    <polygon class="cut" points="136,259 188,259 193,274 193,452 188,468 136,468 131,452 131,274"/>
    <line class="cut-open" x1="131" y1="274" x2="193" y2="274"/>
    <line class="cut-open" x1="131" y1="452" x2="193" y2="452"/>
  </g>
  <g class="side-flap right">
    <polygon class="cut" points="1019,259 1071,259 1076,274 1076,452 1071,468 1019,468 1014,452 1014,274"/>
    <line class="cut-open" x1="1014" y1="274" x2="1076" y2="274"/>
    <line class="cut-open" x1="1014" y1="452" x2="1076" y2="452"/>
  </g>

  <!-- lid flap -->
  <rect class="cut" x="193" y="213" width="821" height="61"/>
  <g class="brand small" transform="translate(604 244)">
    <circle class="brand-dot" cx="-72" cy="0" r="13"/>
    <text class="brand-name" x="-52" y="8" font-size="24">Termivo</text>
  </g>

  <!-- back panel -->
  <rect class="cut" x="193" y="274" width="821" height="178"/>

  <!-- lower inner flap (upside down) -->
  <rect class="cut" x="193" y="452" width="821" height="62"/>
  <g class="brand small" transform="translate(604 480) rotate(180)">
    <circle class="brand-dot" cx="-72" cy="0" r="13"/>
    <text class="brand-name" x="-52" y="8" font-size="24">Termivo</text>
  </g>

  <!-- front panel and base strip with silk background -->
  <rect x="193" y="514" width="821" height="239" fill="url(#silkTone)" role="img" aria-label="Hintergrundfoto: weiß-graue, fließende Seidenstoff-Wellen"/>
  <rect class="cut-open" x="193" y="514" width="821" height="178"/>
  <rect class="cut-open" x="193" y="692" width="821" height="61"/>

  <g class="brand large" transform="translate(604 577)">
    <circle class="brand-dot" cx="-110" cy="0" r="21"/>
    <text class="brand-name" x="-78" y="14" font-size="40">Termivo</text>
  </g>

  <rect class="ribbon" x="193" y="633" width="821" height="37" fill="url(#ribbonTone)"/>
  <text class="band-label" x="604" y="659" text-anchor="middle"><tspan class="light">PRÄZISIONS</tspan><tspan class="strong">THERMOMETER</tspan></text>

  <g class="brand small" transform="translate(604 725)">
    <circle class="brand-dot" cx="-72" cy="0" r="13"/>
    <text class="brand-name" x="-52" y="8" font-size="24">Termivo</text>
  </g>
</svg>
</body>
</html>
```